Business card For real estate appraiser 2

Please see attached pic , need industrial disign card , all word ;ocatiion on the exaplease are aproximate. You are free to move them. one card with 2 sides of information.

```html
<!DOCTYPE html>
<html lang="en">
<head>
<meta charset="utf-8">
<title>Business card – Daniel Rourke</title>
<link href="https://fonts.googleapis.com/css2?family=Montserrat:wght@400;500;600&family=Tinos:wght@700&display=swap" rel="stylesheet">
<style>
  :root {
    --brand-blue: #2389c6;
    --ink: #1b1b1b;
    --ring-grey: #cdcdcd;
    --card-white: #ffffff;
    --page: #eef0f2;
  }
  * { margin: 0; padding: 0; box-sizing: border-box; }
  html, body { width: 1200px; height: 1200px; overflow: hidden; background: var(--page); }
  body { position: relative; font-family: "Montserrat", sans-serif; color: var(--ink); }

  .card { position: absolute; background: var(--card-white); overflow: hidden; }
  .card-front { left: 51px; top: 60px; width: 853px; height: 531px; }
  .card-back { left: 316px; top: 653px; width: 811px; height: 501px; }
  .card-shape { position: absolute; inset: 0; }

  .holder-name {
    position: absolute; font-family: "Tinos", serif; font-weight: 700;
    font-size: 33px; letter-spacing: 0.5px; line-height: 1;
    padding-bottom: 4px; border-bottom: 3px solid var(--ink);
  }
  .holder-title {
    position: absolute; font-size: 15px; font-weight: 500; line-height: 1.45;
    text-transform: uppercase; letter-spacing: 0.3px;
  }
  .rule { position: absolute; height: 3px; background: var(--ink); }

  .contact-row { position: absolute; display: flex; align-items: center; gap: 12px; font-size: 19px; }
  .icon-badge {
    width: 34px; height: 34px; border-radius: 50%; background: var(--brand-blue);
    display: flex; align-items: center; justify-content: center;
  }
  .licence-label { text-decoration: underline; text-underline-offset: 5px; margin-right: 14px; }

  .brand-name {
    position: absolute; display: flex; align-items: center; gap: 12px;
    font-weight: 600; color: var(--brand-blue); line-height: 1.2;
  }
  .brand-square { flex: none; width: 28px; height: 28px; background: var(--brand-blue); }
  .brand-circle { flex: none; width: 46px; height: 46px; border-radius: 50%; background: var(--brand-blue); }

  .website {
    position: absolute; font-size: 16px; font-weight: 500; letter-spacing: 3.2px;
  }

  .licence-grid {
    position: absolute; display: grid; grid-template-columns: auto 3px auto;
    column-gap: 14px; font-size: 16px; line-height: 24px;
  }
  .licence-divider { grid-row: 1 / span 2; grid-column: 2; background: var(--brand-blue); }
  .back-contact { position: absolute; display: flex; align-items: center; gap: 12px; font-size: 16px; }
</style>
</head>
<body>

<section class="card card-front" aria-label="Front of card">
  <svg class="card-shape" viewBox="0 0 853 531" aria-hidden="true">
    <defs>
      <clipPath id="front-lower">
        <rect x="0" y="292" width="853" height="239"/>
      </clipPath>
    </defs>
    <rect x="0" y="290" width="853" height="241" fill="var(--brand-blue)"/>
    <circle cx="170" cy="100" r="270" fill="#fff"/>
    <circle cx="170" cy="100" r="270" fill="none" stroke="var(--ring-grey)" stroke-width="4" clip-path="url(#front-lower)"/>
    <circle cx="760" cy="250" r="390" fill="#fff" stroke="var(--ring-grey)" stroke-width="6"/>
  </svg>

  <div class="brand-name" style="left:84px; top:212px; font-size:25px;">
    <span class="brand-square"></span><span>Harlow Ridge<br>Inspections</span>
  </div>

  <h1 class="holder-name" style="left:469px; top:72px;">DANIEL ROURKE</h1>
  <p class="holder-title" style="left:469px; top:120px;">NYS Licensed<br>Home Inspector</p>
  <span class="rule" style="left:466px; top:174px; width:182px;"></span>

  <div class="contact-row" style="left:440px; top:230px;">
    <span class="icon-badge">
      <svg width="18" height="18" viewBox="0 0 24 24"><path fill="#fff" d="M6.6 10.8a15.1 15.1 0 0 0 6.6 6.6l2.2-2.2a1 1 0 0 1 1-.25 11.4 11.4 0 0 0 3.6.57 1 1 0 0 1 1 1V20a1 1 0 0 1-1 1A17 17 0 0 1 3 4a1 1 0 0 1 1-1h3.5a1 1 0 0 1 1 1c0 1.25.2 2.45.57 3.57a1 1 0 0 1-.25 1z"/></svg>
    </span>555-013-2748
  </div>
  <div class="contact-row" style="left:440px; top:283px;">
    <span class="icon-badge">
      <svg width="20" height="20" viewBox="0 0 24 24" fill="none" stroke="#fff" stroke-width="1.6"><circle cx="12" cy="12" r="9"/><ellipse cx="12" cy="12" rx="4" ry="9"/><path d="M3 12h18M5 7h14M5 17h14"/></svg>
    </span>inspect@harlowridge.example
  </div>
  <div class="contact-row" style="left:444px; top:340px;">
    <span class="licence-label">License #</span>16000047193
  </div>

  <p class="website" style="left:63px; top:498px;">www.harlowridge.example</p>
</section>

<section class="card card-back" aria-label="Back of card">
  <svg class="card-shape" viewBox="0 0 811 501" aria-hidden="true">
    <path d="M0 240 Q405 590 811 250 L811 501 L0 501 Z" fill="var(--brand-blue)"/>
    <path d="M0 240 Q405 590 811 250" fill="none" stroke="var(--ring-grey)" stroke-width="6"/>
  </svg>

  <div class="brand-name" style="left:54px; top:160px; font-size:26px;">
    <span class="brand-circle"></span>Valuecrest.example
  </div>

  <h2 class="holder-name" style="left:421px; top:48px; font-size:27px;">DANIEL ROURKE</h2>
  <p class="holder-title" style="left:421px; top:90px; font-size:14px;">Certified Residential<br>Real Estate Appraiser</p>
  <span class="rule" style="left:421px; top:153px; width:170px;"></span>

  <div class="licence-grid" style="left:421px; top:180px;">
    <span>CA 3008154</span>
    <span class="licence-divider"></span>
    <span>NJ 42RC00391520</span>
    <span>FL RD 4627</span>
    <span>NY 45000076218</span>
  </div>
  <span class="rule" style="left:421px; top:253px; width:170px;"></span>

  <div class="back-contact" style="left:421px; top:268px;">
    <svg width="20" height="20" viewBox="0 0 24 24"><path fill="var(--ink)" d="M6.6 10.8a15.1 15.1 0 0 0 6.6 6.6l2.2-2.2a1 1 0 0 1 1-.25 11.4 11.4 0 0 0 3.6.57 1 1 0 0 1 1 1V20a1 1 0 0 1-1 1A17 17 0 0 1 3 4a1 1 0 0 1 1-1h3.5a1 1 0 0 1 1 1c0 1.25.2 2.45.57 3.57a1 1 0 0 1-.25 1z"/></svg>
    <span style="font-size:18px;">555-013-2748</span>
  </div>
  <div class="back-contact" style="left:421px; top:299px;">
    <svg width="20" height="20" viewBox="0 0 24 24" fill="none" stroke="var(--ink)" stroke-width="1.8"><circle cx="12" cy="12" r="9"/><ellipse cx="12" cy="12" rx="4" ry="9"/><path d="M3 12h18M5 7h14M5 17h14"/></svg>
    dan@valuecrest.example
  </div>

  <p class="website" style="left:278px; top:472px; font-size:15px;">www.harlowridge.example</p>
</section>

</body>
</html>
```